Medical Centre Website

We need a new design for a medical centre based in Perth, Western Australia called 'Tarvin Grove Medical Centre'.

The medical centre does general practitioner work including general checkups, ecg, heart checks, woman's health and more servicing children and adults. They also do home visits on occasions where the patient cannot attend the centre.

They would like an information/brochure website where visitors can read up on the practice, send email and view their location.

The client wish the design to be clean, fresh and light. The main colours are a light purple/blue and to a dark navy blue. The client would not want the logo to be altered in any way. This includes changing the words colours or the image.

The final design should represent a loving, family friendly practice where patients can come to receive the best treatments.

We just need the end product to be presented to un in a layed psd format. The fonts must be as per the W3C standards.

**IMPORTANT**
I have received heaps of chatlink invites in the past. To treat everyone fairly, I do not add people to my chatlink list as in the past people expected us to give them the prize. If you have questions, please ask them in pixel forum as it may benefit others who are also designing the site. If I need to, I will send a message to the user.
Updates

Hi Designers,

Most designs we have received have been overly cluttered. Are you able to simplify the designs.

Cheers, Dorian

Hi Designers,

Some of the designs are quite attractive but aremore cluttered than I would like. If you have a look at the following design, the design is very simple and straight to the point. A lot of designs have too much wording and the reader can be put off. We are looking something more like:

velmoxa.com.au

I would prefer to see designs and have opened up the contest for a further 7 days.

Designers,

We have received feedback from the client and Quite frankly he don’t really like any of them.They are too cluttered and Americanised. All drab blue colours.
 
If you have a look at template monster, these designs are better and cleaner. We do not want heaps of writing on the front page.

If you look at the eariler examples such as quorbeyclinic.com.au which I did myself, the client loves that simplicity of the site.

```html
<!DOCTYPE html>
<html lang="en">
<head>
<meta charset="utf-8">
<title>Tarvin Grove Medical Centre – About Us</title>
<link rel="stylesheet" href="https://fonts.googleapis.com/css2?family=PT+Sans:wght@400;700&family=Noto+Sans:wght@400;700&display=swap">
<style>
  :root {
    --brand-blue: #1a5fb0;
    --heading-blue: #0b5aa8;
    --nav-lilac: #94a7d8;
    --cta-blue: #2b73b8;
    --panel-grey: #dfe0e2;
    --body-text: #444444;
    --rule-grey: #bdbdbd;
    --social-blue: #3f60b3;
    --white: #ffffff;
  }
  * { box-sizing: border-box; margin: 0; padding: 0; }
  html, body { width: 1200px; height: 1000px; overflow: hidden; background: var(--white); }
  body { position: relative; font-family: "Noto Sans", Tahoma, sans-serif; color: var(--body-text); }

  .brand {
    position: absolute; left: 178px; top: 38px;
    color: var(--brand-blue); font-family: "PT Sans", sans-serif; font-weight: 400;
  }
  .brand-name { display: block; font-size: 42px; line-height: 46px; letter-spacing: 0.5px; }
  .brand-sub { display: block; margin-left: 163px; font-size: 22px; line-height: 28px; letter-spacing: 3.5px; }

  .social { position: absolute; top: 25px; left: 947px; display: flex; gap: 10px; }
  .social-link { width: 32px; height: 32px; border-radius: 50%; background: var(--social-blue); display: block; }

  .main-nav {
    position: absolute; left: 128px; top: 128px; width: 940px; height: 46px;
    background: var(--nav-lilac); font-family: "PT Sans", sans-serif; font-size: 17px; color: var(--white);
  }
  .main-nav a, .main-nav .sep { position: absolute; top: 12px; color: var(--white); text-decoration: none; }

  .hero {
    position: absolute; left: 128px; top: 174px; width: 940px; height: 234px;
    border-bottom-left-radius: 56px;
    background: linear-gradient(100deg, #e9edf2 0%, #cfd9e6 30%, #b9c9dc 55%, #e2e8ee 80%, #f1f3f6 100%);
  }

  .appointment { position: absolute; left: 819px; top: 345px; width: 249px; }
  .appointment-title {
    height: 63px; background: var(--cta-blue); color: var(--white);
    font-family: "PT Sans", sans-serif; font-weight: 400; font-size: 22px; line-height: 63px; padding-left: 17px;
  }
  .appointment-body {
    height: 189px; background: var(--panel-grey); border-bottom-right-radius: 12px;
    padding: 20px 19px; color: var(--heading-blue); font-family: "PT Sans", sans-serif; font-size: 21px; line-height: 26px;
  }
  .appointment-phone { display: block; font-family: "Noto Sans", sans-serif; font-weight: 700; font-size: 25px; line-height: 30px; margin-bottom: 8px; }

  .about { position: absolute; left: 181px; top: 428px; width: 596px; }
  .about-title { font-family: "PT Sans", sans-serif; font-weight: 400; font-size: 26px; line-height: 32px; color: var(--heading-blue); margin-bottom: 14px; }
  .staff-role { font-size: 13.5px; font-weight: 700; color: var(--heading-blue); line-height: 18px; }
  .staff-text { font-size: 13.2px; line-height: 18px; text-align: justify; margin-bottom: 18px; }
  .staff-text.is-truncated { height: 36px; overflow: hidden; margin-bottom: 0; }

  .footer-rule { position: absolute; left: 0; top: 875px; width: 1200px; height: 1px; background: var(--rule-grey); }
</style>
</head>
<body>
  <header>
    <div class="brand">
      <span class="brand-name">Tarvin Grove</span>
      <span class="brand-sub">MEDICAL CENTRE</span>
    </div>
    <nav class="social" aria-label="Social links">
      <a class="social-link" href="#" aria-label="Social profile"></a>
      <a class="social-link" href="#" aria-label="Social profile"></a>
      <a class="social-link" href="#" aria-label="News feed"></a>
    </nav>
    <nav class="main-nav" aria-label="Main">
      <a href="#" style="left:52px">Home</a>
      <span class="sep" style="left:142px">|</span>
      <a href="#" style="left:193px">About Us</a>
      <span class="sep" style="left:296px">|</span>
      <a href="#" style="left:347px">Our Services</a>
      <span class="sep" style="left:486px">|</span>
      <a href="#" style="left:537px">Make a Appointment</a>
      <span class="sep" style="left:734px">|</span>
      <a href="#" style="left:785px">Contact Us</a>
    </nav>
  </header>

  <div class="hero" role="img" aria-label="Photo of the smiling medical team in white coats and scrubs"></div>

  <aside class="appointment">
    <h2 class="appointment-title">Make an Appointment</h2>
    <div class="appointment-body">
      Call us
      <span class="appointment-phone">08 5550 2174</span>
      or click to make<br>an appointment via<br>our secure link.
    </div>
  </aside>

  <main class="about">
    <h1 class="about-title">ABOUT US</h1>
    <h3 class="staff-role">Our Doctors</h3>
    <p class="staff-text">There are many variations of passages of Lorem Ipsum available, but the majority have suffered alteration in some form, by injected humour, or randomised words which don't look even slightly believable. If you are going to use a passage of Lorem Ipsum, you need to be sure there isn't anything embarrassing hidden in the middle of text.</p>
    <h3 class="staff-role">Registered Nurse</h3>
    <p class="staff-text">All the Lorem Ipsum generators on the Internet tend to repeat predefined chunks as necessary, making this the first true generator on the Internet. There are many variations of passages of Lorem Ipsum available.</p>
    <h3 class="staff-role">Medical Receptionist And Customer Service</h3>
    <p class="staff-text">It uses a dictionary of over 200 Latin words, combined with a handful of model sentence structures, to generate Lorem Ipsum which looks reasonable. The generated Lorem Ipsum is therefore always free from repetition, injected humour, or non-characteristic words etc.</p>
    <h3 class="staff-role">Practice Manager</h3>
    <p class="staff-text is-truncated">There are many variations of passages of Lorem Ipsum available, but the majority have suffered alteration in some form, by injected humour, or randomised words which don't look even slightly believable.</p>
  </main>

  <div class="footer-rule"></div>
</body>
</html>
```